Velvet Crest Car Detailing Brochure

I would like a trifold brochure designed for my car detailing business. The background has to be full black or mostly black with some designing using only colors present in our logo.

Front page must have our logo and name, list of services, a photo and mybe our phone number but no long text.

Inside I want to present each service one by one with its description and a photo representing/showing each service. (I will provide the text below). For photos, use stock photos and I will add come of mines already too.

On the back of the brochure I want to have contact & info: phone number, opening hours, address, website, Instagram.

Outside left I want the text About us and photo/design.

I want the brochure to be neat, professional, easy to read, but at the same time not too boring.

Text:
1. About us
a. the ultimate destination for car care in Geneva. We provide personalized, detail-oriented services that bring out the best in your car. With our expert techniques and dedicated approach, we ensure that your car receives the utmost care and attention. Experience a place where passion meets precision and let us create an exceptional car care experience designed just for you.
2. Services:

DETAILING & HAND WASH

• Comprehensive exterior & interior care
• Personalisation and tailored cleaning packages
• Decontamination
• Premium products
• Attention to detail for a perfect finish

POLISHING

• Eliminates scratches, holograms
• Revives and protects paint
• Ensures lasting gloss
• Enhances paint life
• Preserves car’s value and beauty

CERAMIC TREATMENT

• Durable paint protection
• Water-repellent (hydrophobic) effect
• Easier cleaning, enhanced shine
• Long-term surface safeguarding
• Shields against environmental impacts

DRY ICE WASH

• Innovative, waterless method
• Safe for all car parts
• Deep cleans, removes odors
• Allergen-free, antibacterial
• Gentle, effective
• Advanced cleaning technology

COVERING

• Personalized vehicle styling
• More than 150 colours available
• Clean cut without using a cutter
• High-quality, durable materials
• Custom designs available

PROTECTION FILM

• Invisible, durable shield
• Self-healing technology
• 10-year warranty by QR VONT

DETAILING BOUTIQUE

• Premium brands available
• Buy on site during your visit
• Marble Harbour, Zeb Autos, DRUP Polaro
• Essential for at-home car care
• Perfect for quick touch-ups
(for these three brands you can put their logos

Target Market(s)

Our target market includes car owners of all price ranges, with a special focus on those who are passionate about their vehicles. We cater to clients who value excellent service and results, and seek to maintain their cars in pristine condition.

Industry/Entity Type

Automobile / Car detailing

Colors

Designer to choose colors to be used in the design.

Requirements
Must have
• Brand Consistency: The brochure must adhere to our brand colors and style, particularly utilizing the colors present in our logo. Trifold Layout: The design must be specifically tailored for a trifold brochure format. Legibility: Text must be easy to read against the mostly black background, with appropriate font size and style. Professional Look and Feel: The overall design must convey professionalism while being engaging and not overly complex. Photo representation: each service description should have a phot presenting it.
Should not have
• Overcrowded Design: Avoid cluttering with too much text or too many images. The layout should be clean and easy to navigate. Cartoonish Fonts or Graphics: Avoid using unprofessional or casual fonts and graphics that do not align with the upscale and professional image of our business. Distracting Backgrounds: The background should complement and not overpower the content. Stick to the theme of mostly black with design elements from our logo.

```html
<!DOCTYPE html>
<html lang="en">
<head>
<meta charset="UTF-8">
<title>Velvet Crest Car Detailing – Trifold Brochure</title>
<link rel="stylesheet" href="https://fonts.googleapis.com/css2?family=Unbounded:wght@700;800&family=Poppins:wght@400;500;600;700&display=swap">
<style>
  :root{
    --ink:#0b0b10;
    --ink-soft:#16161e;
    --white:#ffffff;
    --muted:#c9c9d6;
    --pink:#ec2a92;
    --magenta:#c1188c;
    --violet:#6b3bd3;
    --blue:#2f6fdc;
    --sky:#3fa6ee;
    --paper:#e9e9ee;
    --brand-gradient:linear-gradient(120deg,var(--pink) 0%,var(--magenta) 35%,var(--violet) 65%,var(--blue) 100%);
    --head:"Unbounded", "Arial Black", sans-serif;
    --body:"Poppins", Arial, sans-serif;
  }
  *{box-sizing:border-box;margin:0;padding:0}
  html,body{width:755px;height:1200px;overflow:hidden}
  body{background:var(--paper);font-family:var(--body);color:var(--white);position:relative}

  .sheet{position:absolute;left:20px;width:715px;height:553px;display:grid;grid-template-columns:repeat(3,1fr);background:var(--ink);box-shadow:0 6px 18px rgba(0,0,0,.18);overflow:hidden}
  .sheet--outside{top:30px}
  .sheet--inside{top:617px}
  .panel{position:relative;overflow:hidden;display:flex;flex-direction:column}
  .panel + .panel{border-left:1px solid rgba(255,255,255,.04)}

  .photo{width:100%;flex:none}
  .brand-band{background:var(--brand-gradient);flex:none}

  /* About panel */
  .about .brand-band{height:58px;clip-path:polygon(0 0,100% 0,100% 45%,0 100%)}
  .about__body{padding:14px 20px 0}
  .heading{font-family:var(--head);font-weight:800;text-transform:uppercase;letter-spacing:.5px;line-height:1.05}
  .about .heading{font-size:19px;margin-bottom:6px}
  .rule{width:46px;height:3px;background:var(--pink);margin-bottom:12px}
  .about__text{font-size:8.3px;line-height:1.6;color:var(--muted);margin-bottom:9px}
  .about__photo{margin-top:auto;height:170px;background:linear-gradient(150deg,#2a2a30 0%,#c9681c 45%,#f29a2e 60%,#1a1a20 100%);border-top:4px solid var(--pink)}

  /* Contact panel */
  .contact__photo{height:200px;background:linear-gradient(160deg,#4a5366 0%,#8c93a3 40%,#2a2f3b 100%)}
  .contact__body{padding:18px 20px 0;flex:1;display:flex;flex-direction:column}
  .contact .heading{font-size:19px;margin-bottom:6px}
  .contact-list{list-style:none;display:flex;flex-direction:column;gap:9px}
  .contact-item{display:flex;align-items:flex-start;gap:8px;font-size:8.5px;line-height:1.4}
  .contact-item svg{width:11px;height:11px;flex:none;margin-top:1px}
  .contact-item strong{display:block;font-weight:600;text-transform:uppercase;font-size:8px;letter-spacing:.4px}
  .signature{margin-top:auto;padding-bottom:16px;display:flex;flex-direction:column;gap:8px}
  .mark{display:flex;align-items:center;gap:7px}
  .mark__dot{width:22px;height:22px;border-radius:50%;background:var(--pink);flex:none}
  .mark__name{font-family:var(--body);font-weight:600;font-size:9px;color:var(--white);line-height:1.2}
  .web{display:flex;align-items:center;gap:6px;font-size:8.5px;font-weight:500}
  .web svg{width:10px;height:10px}

  /* Cover panel */
  .cover__photo{height:272px;background:linear-gradient(170deg,#2c3442 0%,#7d889c 45%,#d5dbe6 60%,#3a4150 100%)}
  .cover__mark{display:flex;flex-direction:column;align-items:center;gap:6px;margin-top:-30px;position:relative}
  .cover__mark .mark__dot{width:58px;height:58px;border:4px solid var(--ink)}
  .cover__mark .mark__name{font-size:10px;text-align:center}
  .cover__band{margin-top:auto;height:175px;background:var(--brand-gradient);clip-path:polygon(0 22%,100% 0,100% 100%,0 100%);padding:58px 20px 0;display:flex;flex-direction:column;align-items:flex-end;text-align:right}
  .tagline{font-family:var(--head);font-weight:700;font-size:15px;line-height:1.2}
  .tagline span{display:block;font-weight:800;font-size:17px}
  .cover__band .web{margin-top:14px}

  /* Inside sheet */
  .inside-top{position:absolute;left:0;top:0;width:100%;height:92px;background:var(--brand-gradient);clip-path:polygon(0 0,100% 0,100% 55%,0 100%)}
  .services-title{position:absolute;left:24px;top:22px;font-family:var(--head);font-weight:800;font-size:34px;letter-spacing:2px;color:var(--white)}
  .inside .panel{padding:98px 12px 14px;gap:9px}
  .service-photo{border-radius:3px;flex:none}
  .service{background:var(--ink-soft);border-radius:4px;overflow:hidden;flex:none}
  .service__title{background:var(--brand-gradient);font-family:var(--head);font-weight:700;font-size:7.6px;letter-spacing:.4px;padding:5px 8px;text-transform:uppercase}
  .service__row{display:flex;gap:7px;padding:6px 8px 7px}
  .service__list{list-style:none;flex:1;display:flex;flex-direction:column;gap:2px}
  .service__list li{font-size:6.7px;line-height:1.35;color:var(--muted);padding-left:8px;position:relative}
  .service__list li::before{content:"";position:absolute;left:0;top:3px;width:4px;height:4px;border-radius:50%;background:var(--pink)}
  .service__thumb{width:56px;border-radius:3px;flex:none}
  .brands{display:grid;grid-template-columns:repeat(3,1fr);gap:5px;margin-top:auto}
  .brand{height:34px;border-radius:3px;background:var(--white);color:var(--ink);font-family:var(--body);font-weight:600;font-size:7px;display:flex;align-items:center;justify-content:center;text-align:center;line-height:1.2;padding:0 3px}
</style>
</head>
<body>

<section class="sheet sheet--outside" aria-label="Brochure outside">
  <article class="panel about">
    <div class="brand-band"></div>
    <div class="about__body">
      <h2 class="heading">About us</h2>
      <div class="rule"></div>
      <p class="about__text">The ultimate destination for car care in Geneva. We provide personalized, detail-oriented services that bring out the best in your car.</p>
      <p class="about__text">With our expert techniques and dedicated approach, we ensure that your car receives the utmost care and attention.</p>
      <p class="about__text">Experience a place where passion meets precision and let us create an exceptional car care experience designed just for you.</p>
    </div>
    <div class="photo about__photo" role="img" aria-label="Photo of an orange sports car bonnet being detailed"></div>
  </article>

  <article class="panel contact">
    <div class="photo contact__photo" role="img" aria-label="Photo of a wash mitt cleaning a car's paintwork"></div>
    <div class="contact__body">
      <h2 class="heading">Contact us</h2>
      <div class="rule"></div>
      <ul class="contact-list">
        <li class="contact-item">
          <svg viewBox="0 0 24 24" fill="var(--pink)"><path d="M6.6 10.8a15.1 15.1 0 0 0 6.6 6.6l2.2-2.2a1 1 0 0 1 1-.25 11.4 11.4 0 0 0 3.6.57 1 1 0 0 1 1 1V20a1 1 0 0 1-1 1A17 17 0 0 1 3 4a1 1 0 0 1 1-1h3.5a1 1 0 0 1 1 1c0 1.25.2 2.45.57 3.57a1 1 0 0 1-.25 1z"/></svg>
          <span>(+41) 22 555 01 47</span>
        </li>
        <li class="contact-item">
          <svg viewBox="0 0 24 24" fill="var(--pink)"><path d="M12 2a7 7 0 0 0-7 7c0 5.25 7 13 7 13s7-7.75 7-13a7 7 0 0 0-7-7zm0 9.5A2.5 2.5 0 1 1 12 6.5a2.5 2.5 0 0 1 0 5z"/></svg>
          <span>14 Rue des Lilas,<br>1205 Geneva</span>
        </li>
        <li class="contact-item">
          <svg viewBox="0 0 24 24" fill="none" stroke="var(--pink)" stroke-width="2.4"><circle cx="12" cy="12" r="9"/><path d="M12 7v5l3 2"/></svg>
          <span><strong>Opening hours</strong>Mon – Fri: 8am – 7pm</span>
        </li>
      </ul>
      <div class="signature">
        <div class="mark"><span class="mark__dot"></span><span class="mark__name">Velvet Crest<br>Car Detailing</span></div>
        <div class="web">
          <svg viewBox="0 0 24 24" fill="none" stroke="var(--pink)" stroke-width="2.2"><circle cx="12" cy="12" r="9"/><path d="M3 12h18M12 3c3 3.5 3 14.5 0 18M12 3c-3 3.5-3 14.5 0 18"/></svg>
          www.velvetcrestdetail.ch
        </div>
      </div>
    </div>
  </article>

  <article class="panel cover">
    <div class="photo cover__photo" role="img" aria-label="Photo of a car covered in foam during a hand wash"></div>
    <div class="cover__mark">
      <span class="mark__dot"></span>
      <span class="mark__name">Velvet Crest Car Detailing</span>
    </div>
    <div class="cover__band">
      <p class="tagline">The ultimate destination for <span>CAR CARE</span></p>
      <div class="web">
        <svg viewBox="0 0 24 24" fill="none" stroke="var(--white)" stroke-width="2.2"><circle cx="12" cy="12" r="9"/><path d="M3 12h18M12 3c3 3.5 3 14.5 0 18M12 3c-3 3.5-3 14.5 0 18"/></svg>
        www.velvetcrestdetail.ch
      </div>
    </div>
  </article>
</section>

<section class="sheet sheet--inside inside" aria-label="Brochure inside">
  <div class="inside-top"></div>
  <h1 class="services-title">SERVICES:</h1>

  <div class="panel">
    <div class="service-photo" style="height:120px;background:linear-gradient(150deg,#1d1d24,#5b5f6b 50%,#23232b)" role="img" aria-label="Photo of a car interior with steering wheel being cleaned"></div>
    <div class="service">
      <h3 class="service__title">Detailing &amp; hand wash</h3>
      <div class="service__row">
        <ul class="service__list">
          <li>Comprehensive exterior &amp; interior care</li>
          <li>Personalisation and tailored cleaning packages</li>
          <li>Decontamination</li>
          <li>Premium products</li>
          <li>Attention to detail for a perfect finish</li>
        </ul>
      </div>
    </div>
    <div class="service-photo" style="height:110px;background:linear-gradient(150deg,#1a2a4a,#3a78c8 50%,#cfd8e6)" role="img" aria-label="Photo of a blue polishing pad on car paint"></div>
    <div class="service">
      <h3 class="service__title">Polishing</h3>
      <div class="service__row">
        <ul class="service__list">
          <li>Eliminates scratches, holograms</li>
          <li>Revives and protects paint</li>
          <li>Ensures lasting gloss</li>
          <li>Enhances paint life</li>
          <li>Preserves car’s value and beauty</li>
        </ul>
      </div>
    </div>
  </div>

  <div class="panel">
    <div class="service">
      <h3 class="service__title">Ceramic treatment</h3>
      <div class="service__row">
        <ul class="service__list">
          <li>Durable paint protection</li>
          <li>Water-repellent (hydrophobic) effect</li>
          <li>Easier cleaning, enhanced shine</li>
          <li>Long-term surface safeguarding</li>
          <li>Shields against environmental impacts</li>
        </ul>
        <div class="service__thumb" style="background:linear-gradient(160deg,#20283a,#6f8fb8)" role="img" aria-label="Photo of water beading on ceramic-coated paint"></div>
      </div>
    </div>
    <div class="service">
      <h3 class="service__title">Dry ice wash</h3>
      <div class="service__row">
        <ul class="service__list">
          <li>Innovative, waterless method</li>
          <li>Safe for all car parts</li>
          <li>Deep cleans, removes odors</li>
          <li>Allergen-free, antibacterial</li>
          <li>Gentle, effective</li>
          <li>Advanced cleaning technology</li>
        </ul>
        <div class="service__thumb" style="background:linear-gradient(160deg,#3a3f48,#d9dee6)" role="img" aria-label="Photo of dry ice cleaning an engine bay"></div>
      </div>
    </div>
    <div class="service">
      <h3 class="service__title">Covering</h3>
      <div class="service__row">
        <ul class="service__list">
          <li>Personalized vehicle styling</li>
          <li>More than 150 colours available</li>
          <li>Clean cut without using a cutter</li>
          <li>High-quality, durable materials</li>
          <li>Custom designs available</li>
        </ul>
        <div class="service__thumb" style="background:linear-gradient(160deg,#5a1a4a,#c1188c)" role="img" aria-label="Photo of a car being wrapped in coloured vinyl"></div>
      </div>
    </div>
  </div>

  <div class="panel">
    <div class="service">
      <h3 class="service__title">Protection film</h3>
      <div class="service__row">
        <ul class="service__list">
          <li>Invisible, durable shield</li>
          <li>Self-healing technology</li>
          <li>10-year warranty by QR VONT</li>
        </ul>
        <div class="service__thumb" style="background:linear-gradient(160deg,#2a2e36,#9aa3b2)" role="img" aria-label="Photo of clear protection film applied to a bumper"></div>
      </div>
    </div>
    <div class="service-photo" style="height:96px;background:linear-gradient(150deg,#1c1c22,#4b4f5a 55%,#1c1c22)" role="img" aria-label="Photo of the detailing boutique shelves with care products"></div>
    <div class="service">
      <h3 class="service__title">Detailing boutique</h3>
      <div class="service__row">
        <ul class="service__list">
          <li>Premium brands available</li>
          <li>Buy on site during your visit</li>
          <li>Marble Harbour, Zeb Autos, DRUP Polaro</li>
          <li>Essential for at-home car care</li>
          <li>Perfect for quick touch-ups</li>
        </ul>
      </div>
    </div>
    <div class="brands">
      <div class="brand">Marble Harbour</div>
      <div class="brand">Zeb Autos</div>
      <div class="brand">DRUP Polaro</div>
    </div>
  </div>
</section>

</body>
</html>
```